Professional and creative business card design for recruiting service providers

Our company supports German medium-sized companies in filling vacancies promptly. For this we use social media marketing and bring our customers into the visibility.

We want a professional but also creative design for our business cards.

Please look at halvenrick-consult.de to get an impression of our CI.

Target Market(s)

Small and medium-sized companies in Germany from the industry

Industry/Entity Type

Industrie, Handwerk

Contact Information for Business Card

Name, Position, Telefonnummer, Email, Website

Colors
EE7325
F08F49
F5BC92
FAE3D3
FDF4ED

Requirements
Must have
• A picture of the employee and in the style of www.halvenrick-consult.de

```html
<!DOCTYPE html>
<html lang="de">
<head>
<meta charset="utf-8">
<title>Halvenrick Consult – Visitenkarte</title>
<link href="https://fonts.googleapis.com/css2?family=Poppins:wght@300;400;600;700&display=swap" rel="stylesheet">
<style>
  :root{
    --orange:#EE7325;
    --orange-mid:#F08F49;
    --peach:#F5BC92;
    --peach-light:#FAE3D3;
    --cream:#FDF4ED;
    --ink:#111111;
    --white:#ffffff;
    --page:#ffffff;
  }
  *{margin:0;padding:0;box-sizing:border-box}
  html,body{width:1200px;height:1126px;overflow:hidden;background:var(--page)}
  body{font-family:"Poppins",sans-serif;position:relative}
  .card{
    position:absolute;top:409px;width:540px;height:308px;overflow:hidden;
    box-shadow:10px 12px 14px rgba(0,0,0,.45);
  }
  .card--back{
    left:40px;
    background:
      radial-gradient(ellipse 190px 150px at 130px 160px, var(--peach) 0%, rgba(245,188,146,.55) 45%, rgba(250,227,211,0) 100%),
      radial-gradient(ellipse 260px 200px at 340px 80px, var(--cream) 0%, rgba(253,244,237,0) 100%),
      linear-gradient(135deg, var(--peach-light) 0%, var(--cream) 60%, var(--peach-light) 90%, var(--peach) 100%);
  }
  .card--front{left:620px;background:var(--orange);color:var(--white)}
  .brand{position:absolute;display:flex;align-items:center;color:var(--ink);font-weight:700;text-transform:uppercase}
  .brand__mark{background:var(--orange);flex:none}
  .brand--large{left:263px;top:198px;gap:14px}
  .brand--large .brand__mark{width:78px;height:78px}
  .brand--large .brand__name{font-size:25px;line-height:29px}
  .brand--small{left:412px;top:26px;gap:7px}
  .brand--small .brand__mark{width:26px;height:26px;background:var(--ink)}
  .brand--small .brand__name{font-size:10px;line-height:11px}
  .portrait{position:absolute;left:28px;top:66px;width:246px;height:146px;transform:rotate(-6deg)}
  .person{position:absolute;left:48px;bottom:22px}
  .person__name{font-size:30px;line-height:34px;font-weight:300;letter-spacing:.2px}
  .person__name strong{font-weight:700}
  .person__role{font-size:13.5px;font-weight:400}
  .contacts{position:absolute;left:346px;top:160px;list-style:none;font-size:11px;line-height:13px}
  .contacts li{display:flex;align-items:flex-start;gap:9px;margin-bottom:12px}
  .contacts li:last-child{margin-bottom:0}
  .contacts svg{width:14px;height:14px;flex:none;margin-top:-1px}
</style>
</head>
<body>

<section class="card card--back" aria-label="Rückseite">
  <div class="brand brand--large">
    <span class="brand__mark"></span>
    <span class="brand__name">Halvenrick<br>Consult</span>
  </div>
</section>

<section class="card card--front" aria-label="Vorderseite">
  <div class="brand brand--small">
    <span class="brand__mark"></span>
    <span class="brand__name">Halvenrick<br>Consult</span>
  </div>

  <svg class="portrait" viewBox="0 0 246 146" role="img" aria-label="Porträtfoto des Mitarbeiters im Anzug auf einem Bürostuhl">
    <defs>
      <radialGradient id="portraitFill" cx="55%" cy="60%" r="60%">
        <stop offset="0" stop-color="#6b5a52"/>
        <stop offset=".45" stop-color="#3a3633"/>
        <stop offset=".7" stop-color="#bdb8b4"/>
        <stop offset="1" stop-color="#ffffff"/>
      </radialGradient>
    </defs>
    <ellipse cx="123" cy="73" rx="122" ry="72" fill="url(#portraitFill)"/>
  </svg>

  <div class="person">
    <h1 class="person__name">JONAS <strong>VELTEN</strong></h1>
    <p class="person__role">Senior Recruiting Berater</p>
  </div>

  <ul class="contacts">
    <li>
      <svg viewBox="0 0 16 16"><circle cx="8" cy="8" r="8" fill="#fff"/><path d="M5.3 4.2l1.3-.2.8 2-1 .8a6 6 0 0 0 2.8 2.8l.8-1 2 .8-.2 1.3c-.2.5-.8.8-1.4.7A7 7 0 0 1 4.6 5.6c-.1-.6.2-1.2.7-1.4z" fill="var(--orange)"/></svg>
      <span>0172 555 0193</span>
    </li>
    <li>
      <svg viewBox="0 0 16 16"><circle cx="8" cy="8" r="7.3" fill="none" stroke="#fff" stroke-width="1.2"/><rect x="4.3" y="5.3" width="7.4" height="5.4" rx=".6" fill="none" stroke="#fff" stroke-width="1"/><path d="M4.5 5.6L8 8.4l3.5-2.8" fill="none" stroke="#fff" stroke-width="1"/></svg>
      <span>info@halvenrick-consult.de</span>
    </li>
    <li>
      <svg viewBox="0 0 16 16"><circle cx="8" cy="8" r="8" fill="#fff"/><path d="M8 3.5a3 3 0 0 0-3 3c0 2.2 3 5.8 3 5.8s3-3.6 3-5.8a3 3 0 0 0-3-3z" fill="var(--orange)"/><circle cx="8" cy="6.5" r="1.1" fill="#fff"/></svg>
      <span>Halvenrick Consult GmbH<br>Lindenhofer Straße 42<br>70173 Stuttgart</span>
    </li>
    <li>
      <svg viewBox="0 0 16 16" fill="none" stroke="#fff" stroke-width="1"><circle cx="8" cy="8" r="7.3" stroke-width="1.2"/><circle cx="8" cy="8" r="4"/><ellipse cx="8" cy="8" rx="1.7" ry="4"/><path d="M4 8h8"/></svg>
      <span>halvenrick-consult.de</span>
    </li>
  </ul>
</section>

</body>
</html>
```